HRC

This is to hand out to folks at conferences to tell them about this list serve and direct them to the site to email in to join it.
This is a networking and resource site for mental health and addiction professionals.
The mission statement on the ABOUT page needs to be on it.
Then the website address and my name Marta Quillon, LICSW
List Serve Moderator and my email Marta@MartaQuillon.net
and my phone 202-555-0148.
Please see website: www.harborreferralcircle.net

Industry/Entity Type

Mental Health

Contact Information for Business Card

Front: name Harbor Referral Circle and mission statement on the "About" page and put website address: www.harborreferralcircle.net and my name Marta Quillon, LICSW ListServ Moderator
Back: info on the list serve with instructions to go to Contact Us page.
Anything you all think might be useful and still look good.
Put my cell # on the back, 202-555-0193

```html
<!DOCTYPE html>
<html lang="en">
<head>
<meta charset="utf-8">
<title>Harbor Referral Circle – Business Card</title>
<link rel="stylesheet" href="https://fonts.googleapis.com/css2?family=Bodoni+Moda:wght@400;600;700&display=swap">
<style>
  :root {
    --bg: #ecebe8;
    --navy: #1d3a5e;
    --red: #8a2524;
    --red-dark: #6e1b1b;
    --rose: #b8695f;
    --ink: #ffffff;
    --ink-soft: #f1e4e2;
    --star: #8c9bb3;
  }
  * { box-sizing: border-box; margin: 0; padding: 0; }
  html, body { width: 1200px; height: 899px; overflow: hidden; background: var(--bg); }
  body { position: relative; font-family: "Bodoni Moda", "Didot", serif; color: var(--ink); }

  .card {
    position: absolute;
    width: 574px;
    height: 336px;
    background: var(--red);
    overflow: hidden;
    box-shadow: 0 3px 8px rgba(0,0,0,.25);
  }
  .card--front { left: 313px; top: 67px; }
  .card--back  { left: 313px; top: 435px; }

  .card__top {
    position: absolute; left: 0; top: 0; width: 100%; height: 27px;
    background: var(--navy);
  }
  .card__stars {
    position: absolute; right: 8px; top: 6px; width: 124px; height: 14px;
  }
  .card__accent {
    position: absolute; left: 0; top: 60px; width: 90px; height: 170px;
    background: linear-gradient(90deg, rgba(255,255,255,.14), rgba(255,255,255,0));
  }
  .card__title {
    position: absolute; left: 0; top: 33px; width: 100%;
    text-align: center; font-size: 35px; font-weight: 400; letter-spacing: .2px;
  }
  .card__body {
    position: absolute; left: 40px; right: 40px; top: 76px;
    text-align: center; font-size: 12.6px; line-height: 15.4px; color: var(--ink-soft);
  }
  .card__band {
    position: absolute; left: 0; width: 100%; height: 40px;
    background: var(--rose);
    border-bottom: 3px solid var(--red-dark);
    display: flex; align-items: center; justify-content: center; gap: 14px;
  }
  .card--front .card__band { top: 245px; }
  .card--back  .card__band { top: 244px; }
  .card__name { font-size: 32px; font-weight: 700; letter-spacing: -.3px; }
  .card__role { font-size: 18.5px; font-weight: 700; padding-top: 6px; }
  .card__phone { display: flex; align-items: center; gap: 6px; font-size: 29px; font-weight: 600; }
  .card__phone svg { width: 20px; height: 26px; }
  .card__bottom {
    position: absolute; left: 0; bottom: 0; width: 100%; height: 48px;
    background: var(--navy);
    display: flex; align-items: center; justify-content: center;
    font-size: 21px; letter-spacing: .4px;
  }
</style>
</head>
<body>

<section class="card card--front">
  <div class="card__top">
    <div class="card__stars" role="img" aria-label="Row of small stars" style="background:linear-gradient(90deg,rgba(140,155,179,.0),rgba(140,155,179,.45));"></div>
  </div>
  <div class="card__accent" role="img" aria-label="Large faint star decoration"></div>
  <h1 class="card__title">Harbor Referral Circle</h1>
  <p class="card__body">
    The Harbor Referral Circle Listserv began<br>
    on December 10, 2010 with a few names of professionals that<br>
    wanted to keep connection with each other.<br>
    Today the listserv has over 400 members and is growing strong.<br>
    This listserv includes addiction and mental health professionals<br>
    of all kinds from around the country and even one internationally<br>
    that share resources, help each other find the right placements<br>
    for their patients/clients, toss around important issues,<br>
    invite each other to valuable events and much more.
  </p>
  <div class="card__band">
    <span class="card__name">Marta Quillon</span>
    <span class="card__role">LICSW ListServ Moderator</span>
  </div>
  <div class="card__bottom">www.harborreferralcircle.net</div>
</section>

<section class="card card--back">
  <div class="card__top">
    <div class="card__stars" role="img" aria-label="Row of small stars" style="background:linear-gradient(90deg,rgba(140,155,179,.0),rgba(140,155,179,.45));"></div>
  </div>
  <div class="card__accent" role="img" aria-label="Large faint star decoration"></div>
  <h2 class="card__title">Harbor Referral Circle</h2>
  <p class="card__body">
    Joining the Listserv is easy; go to the "Contact Us" tab,<br>
    fill out the form and let us know that you'd like to become a member.<br>
    You will then be sent an invitation to Join the Group<br>
    from Listwell Groups. &nbsp;Next, follow the prompts to<br>
    "Join this Mailing List", there will be two prompts for that.<br>
    You do not need to Join the Group, only JOIN THIS MAILING LIST.<br>
    Once you do that you will receive an email welcoming you to the listserv<br>
    and telling you how to use this wonderful resource.
  </p>
  <div class="card__band">
    <span class="card__name">Marta Quillon</span>
    <span class="card__phone">
      <svg viewBox="0 0 20 26" aria-hidden="true"><path fill="#fff" d="M5 1 L8 1 L9 7 L6.5 8.5 C7.5 12 9 15.5 11.5 18 L14 16.5 L18 21 L16 24.5 C9 25 2.5 14 3 3 Z"/></svg>
      202-555-0193
    </span>
  </div>
  <div class="card__bottom">www.harborreferralcircle.net</div>
</section>

</body>
</html>
```